Australian Software Consultancy needs new Business Card Design

Design Business Card based on existing design artefacts (attached). We are open to all designs. As its a 2 sided design and we thought it might be quite striking to have one side with a black background and te other side with a white background.

Target Market(s)

Financial Services mainly.

Industry/Entity Type

Business

Contact Information for Business Card

Name :
Position :
Email :

Requirements
Must have
• Funky design using our existing assets

```html
<!DOCTYPE html>
<html lang="en">
<head>
<meta charset="utf-8">
<title>Deep Current – Business Card</title>
<link rel="stylesheet" href="https://fonts.googleapis.com/css2?family=Lato:wght@400;700;900&display=swap">
<style>
  :root {
    --stage: #6f7a80;
    --stage-dark: #4d565b;
    --card-white: #ffffff;
    --card-black: #000000;
    --brand-red: #e8242b;
    --ink: #111111;
    --ink-soft: #333333;
  }
  * { box-sizing: border-box; margin: 0; padding: 0; }
  html, body { width: 1200px; height: 900px; overflow: hidden; }
  body {
    background: radial-gradient(ellipse at 50% 60%, var(--stage) 0%, var(--stage-dark) 100%);
    font-family: "Lato", Arial, sans-serif;
    position: relative;
  }
  .card {
    position: absolute;
    left: 320px;
    width: 560px;
    height: 320px;
    overflow: hidden;
    box-shadow: 0 10px 24px rgba(0,0,0,.35);
  }
  .card--front { top: 110px; background: var(--card-white); }
  .card--back  { top: 470px; background: var(--card-black); }

  .edge-band {
    position: absolute; left: 0; top: 0; bottom: 0; width: 18px;
    background: var(--brand-red);
  }
  .edge-band::after {
    content: ""; position: absolute; right: -6px; top: 0; bottom: 0; width: 6px;
    background: var(--ink);
  }
  .icon-tab {
    position: absolute; left: 0; top: 124px; width: 58px; height: 96px;
    background: var(--brand-red);
    clip-path: polygon(0 0, 100% 12%, 100% 88%, 0 100%);
    display: flex; flex-direction: column; justify-content: space-around;
    align-items: center; padding: 12px 0 12px 14px;
  }
  .icon-tab svg { width: 15px; height: 15px; }

  .wordmark {
    position: absolute; left: 74px; top: 44px;
    font-weight: 900; font-size: 38px; letter-spacing: 1px;
    color: var(--ink); text-transform: uppercase;
  }
  .contact-list {
    position: absolute; left: 74px; top: 132px;
    list-style: none; font-size: 15px; color: var(--ink-soft);
    line-height: 28px;
  }

  .person {
    position: absolute; right: 62px; top: 192px; text-align: right;
  }
  .person__name { font-size: 26px; font-weight: 700; color: var(--brand-red); line-height: 1.2; }
  .person__role { font-size: 13px; color: var(--ink-soft); }

  .address {
    position: absolute; right: 62px; top: 260px; text-align: left;
    font-style: normal; font-size: 15px; color: var(--ink-soft); line-height: 20px;
    padding-right: 70px;
  }
  .corner-block {
    position: absolute; right: 0; top: 196px; width: 40px; height: 54px;
    background: var(--brand-red);
  }
  .corner-block::before {
    content: ""; position: absolute; left: -7px; top: 0; bottom: 0; width: 7px;
    background: var(--ink);
  }

  .back-mark {
    position: absolute; inset: 0;
    display: flex; align-items: center; justify-content: center; gap: 22px;
  }
  .back-mark__circle {
    width: 150px; height: 150px; border-radius: 50%;
    border: 14px solid var(--brand-red);
    flex: none;
  }
  .back-mark__name {
    font-weight: 900; font-size: 38px; color: var(--brand-red);
    text-transform: uppercase; letter-spacing: 1px; white-space: nowrap;
  }
</style>
</head>
<body>
  <section class="card card--front" aria-label="Business card front">
    <div class="edge-band"></div>
    <div class="icon-tab">
      <svg viewBox="0 0 24 24" fill="#fff" aria-hidden="true"><path d="M6.6 10.8a15.1 15.1 0 0 0 6.6 6.6l2.2-2.2c.3-.3.7-.4 1-.2 1.1.4 2.3.6 3.6.6.6 0 1 .4 1 1V20c0 .6-.4 1-1 1C10.6 21 3 13.4 3 4c0-.6.4-1 1-1h3.5c.6 0 1 .4 1 1 0 1.3.2 2.5.6 3.6.1.3 0 .7-.2 1z"/></svg>
      <svg viewBox="0 0 24 24" fill="#fff" aria-hidden="true"><path d="M3 5h18v14H3z M3 5l9 7 9-7" stroke="#e8242b" stroke-width="1.5"/></svg>
      <svg viewBox="0 0 24 24" fill="none" stroke="#fff" stroke-width="2" aria-hidden="true"><circle cx="12" cy="12" r="9"/><path d="M3 12h18M12 3c3 3.5 3 14.5 0 18M12 3c-3 3.5-3 14.5 0 18"/></svg>
    </div>
    <div class="wordmark">Deep Current</div>
    <ul class="contact-list">
      <li>555-010-2040</li>
      <li>hello@deepcurrent.com</li>
      <li>www.deepcurrent.com</li>
    </ul>
    <div class="person">
      <div class="person__name">Corin Vale</div>
      <div class="person__role">Owner</div>
    </div>
    <div class="corner-block"></div>
    <address class="address">48 Harbour Lane<br>Sydney NSW 2000</address>
  </section>

  <section class="card card--back" aria-label="Business card back">
    <div class="back-mark">
      <div class="back-mark__circle"></div>
      <div class="back-mark__name">Deep Current</div>
    </div>
  </section>
</body>
</html>
```